Engineering group involved with fire safety needs a business card

We need a business card design for a company based in Greece called "Varotis Group". We are engineers and specialized technicians, operating the following : a) Fire fighting equipment trade b) Installation , Inspection & Maintenance of fire extinguishers and fire protection systems c) Occupational Health & Safety (Risk assessment & management/ Staff training). We need a clear and simple card design. I uploaded a draft I made, in order to give you an idea of the company and how I currently imagine the design of the card. I also uploaded the logo in .png file format. We are always open to different, new suggestions and ideas you may want to submit.
Target Market(s)
industries, companies, managers, retail clients
Industry/Entity Type
Fire Safety
Contact Information for Business Card
Addresses & phone numbers (headquarters + branch), logo, name (you can find all the details on the uploaded files!)
Colors
Designer to choose colors to be used in the design.
Look and feel
Each slider illustrates characteristics of the customer's brand and the style your logo design should communicate.

```html
<!DOCTYPE html>
<html lang="en">
<head>
<meta charset="utf-8">
<title>Varotis Group – Business Card</title>
<link rel="stylesheet" href="https://fonts.googleapis.com/css2?family=Montserrat:wght@700;800&family=Open+Sans:wght@400;600&display=swap">
<style>
  :root {
    --backdrop: #e9e7e4;
    --card-white: #ffffff;
    --card-black: #121212;
    --brand-red: #b8202b;
    --band-red: #c4343c;
    --band-grey: #6d6f72;
    --text-grey: #5d5f62;
    --text-dark: #3d3f42;
    --shadow: rgba(0, 0, 0, 0.18);
  }
  * { box-sizing: border-box; margin: 0; padding: 0; }
  html, body {
    width: 1200px; height: 900px; overflow: hidden;
    background: var(--backdrop);
  }
  .canvas {
    position: relative; width: 1200px; height: 900px;
    display: flex; flex-direction: column; align-items: center; justify-content: center; gap: 28px;
  }
  .card {
    position: relative; width: 640px; height: 366px; overflow: hidden;
    box-shadow: 0 10px 28px var(--shadow);
  }

  /* Back side */
  .card--back {
    background: var(--card-black);
    display: flex; align-items: center; justify-content: center;
  }
  .brand-back {
    display: flex; align-items: center; gap: 18px;
    font-family: "Montserrat", sans-serif; font-weight: 800;
    font-size: 52px; letter-spacing: 3px; color: var(--card-white);
    text-transform: uppercase;
  }
  .brand-back__square { width: 34px; height: 34px; background: var(--card-white); }

  /* Front side */
  .card--front { background: var(--card-white); }
  .brand-front {
    position: absolute; left: 40px; top: 44px;
    display: flex; align-items: center; gap: 10px;
    font-family: "Montserrat", sans-serif; font-weight: 800;
    font-size: 27px; letter-spacing: 1px; color: var(--brand-red);
    text-transform: uppercase;
  }
  .brand-front__square { width: 18px; height: 18px; background: var(--brand-red); }
  .contact-list {
    position: absolute; left: 40px; top: 112px; list-style: none;
    font-family: "Open Sans", sans-serif; font-size: 16px; color: var(--text-dark);
  }
  .contact-list li { display: flex; align-items: center; gap: 12px; height: 31px; }
  .contact-list li.contact-phone { margin-left: -2px; height: 28px; margin-bottom: 4px; }
  .contact-icon { width: 20px; height: 20px; flex: none; }
  .person {
    position: absolute; right: 40px; top: 140px; text-align: right;
  }
  .person__name {
    font-family: "Montserrat", sans-serif; font-weight: 700;
    font-size: 24px; color: var(--brand-red); line-height: 1.1;
  }
  .person__role {
    font-family: "Open Sans", sans-serif; font-weight: 400;
    font-size: 23px; color: var(--text-grey); line-height: 1.2;
  }
  .footer-bands { position: absolute; left: 0; bottom: 0; width: 640px; height: 110px; }
</style>
</head>
<body>
<main class="canvas">
  <section class="card card--back" aria-label="Business card, back side">
    <div class="brand-back"><span class="brand-back__square"></span>Varotis Group</div>
  </section>

  <section class="card card--front" aria-label="Business card, front side">
    <div class="brand-front"><span class="brand-front__square"></span>Varotis Group</div>

    <ul class="contact-list">
      <li class="contact-phone">
        <span>+302104817362</span>
      </li>
      <li>
        <svg class="contact-icon" viewBox="0 0 20 20" aria-hidden="true">
          <rect x="0.5" y="0.5" width="19" height="19" rx="3" fill="none" stroke="var(--brand-red)"/>
          <path d="M6 4.5c1 0 1.5 2 2 3l-1 1.2c.6 1.5 1.8 2.7 3.3 3.3l1.2-1c1 .5 3 1 3 2 0 1-1 2-2 2C8 15 5 12 4 7.5c0-1 1-3 2-3z" fill="var(--brand-red)"/>
        </svg>
        <span>info@varotisgroup.gr</span>
      </li>
      <li>
        <svg class="contact-icon" viewBox="0 0 20 20" aria-hidden="true">
          <rect x="0.5" y="0.5" width="19" height="19" rx="3" fill="none" stroke="var(--brand-red)"/>
          <path d="M4 6h12v8H4z" fill="var(--brand-red)"/>
          <path d="M4 6l6 4.5L16 6" fill="none" stroke="#fff" stroke-width="1.2"/>
        </svg>
        <span>www.varotisgroup.gr</span>
      </li>
      <li>
        <svg class="contact-icon" viewBox="0 0 20 20" aria-hidden="true">
          <rect x="0.5" y="0.5" width="19" height="19" rx="3" fill="none" stroke="var(--brand-red)"/>
          <circle cx="10" cy="10" r="6" fill="var(--brand-red)"/>
          <path d="M4 10h12M10 4c-2.5 3-2.5 9 0 12M10 4c2.5 3 2.5 9 0 12" fill="none" stroke="#fff" stroke-width="0.9"/>
        </svg>
        <span>12 Anemonis Street</span>
      </li>
      <li>
        <svg class="contact-icon" viewBox="0 0 20 20" aria-hidden="true">
          <rect x="0.5" y="0.5" width="19" height="19" rx="3" fill="none" stroke="var(--brand-red)"/>
          <path d="M10 4l6 5.5h-2V16h-3v-4H9v4H6V9.5H4z" fill="var(--brand-red)"/>
        </svg>
        <span>Athens, Greece</span>
      </li>
    </ul>

    <div class="person">
      <p class="person__name">Stavros Kalamaris</p>
      <p class="person__role">Director</p>
    </div>

    <svg class="footer-bands" viewBox="0 0 640 110" preserveAspectRatio="none" aria-hidden="true">
      <path d="M0 96 L330 62 Q360 58 380 40 L400 22 Q410 14 430 14 L640 14 L640 110 L0 110 Z" fill="var(--band-grey)"/>
      <path d="M0 104 L340 72 Q370 68 390 48 L405 30 Q415 22 435 22 L640 22 L640 110 L0 110 Z" fill="var(--band-red)"/>
    </svg>
  </section>
</main>
</body>
</html>
```